Signage for a foam car wash facility

We need signages done for a foam car wash.
We use only premium, environment-friendly, biodegradable foam wash and cleaning products.
We are in a commercial center (mall) situated in an upscale part of town and need our signage to reflect that.
We need signages for directions (two or three smaller ones), one showing that we are here, and at the actual car wash.
We will provide our logo, the texts, some pictures of the actual location the dimensions of the signages.
We need the signages to be informative, clean, crisp, modern with the use of icons if possible and some colour so that we get the attention of clients passing -by without being too flashy.
Directions to the car wash should look like a petal of a flower directing towards the car wash

Target Market(s)

Upscale market with a school and a gym next to it. Mom and dad's dropping their children at school, offices nearby.

Industry/Entity Type

Car Wash

Requirements
Nice to have
• icons, some colors,Directions to the car wash should look like a petal of a flower directing towards the car wash

```html
<!DOCTYPE html>
<html lang="en">
<head>
<meta charset="utf-8">
<title>VERDALIA Foam Car Wash Signage</title>
<link href="https://fonts.googleapis.com/css2?family=Montserrat:wght@500;600;700;800&display=swap" rel="stylesheet">
<style>
  :root {
    --backdrop: #231f20;
    --sign-green: #9bae33;
    --lime: #a6c23a;
    --teal: #5cb894;
    --teal-text: #3e8f72;
    --white: #ffffff;
    --ink: #111111;
    --photo-dark: #3a4046;
    --photo-light: #d9dde0;
  }
  html, body {
    margin: 0;
    padding: 0;
    width: 1200px;
    height: 1200px;
    overflow: hidden;
    background: var(--backdrop);
  }
  .signage-sheet { display: block; width: 1200px; height: 1200px; }
  .brand-name { font-family: "Montserrat", sans-serif; font-weight: 600; }
  .headline { font-family: "Montserrat", sans-serif; font-weight: 800; }
  .caption { font-family: "Montserrat", sans-serif; font-weight: 700; }
  .panel-white { fill: var(--white); }
  .panel-green { fill: var(--sign-green); }
  .band-teal { fill: var(--teal); }
  .fill-white { fill: var(--white); }
  .fill-teal-text { fill: var(--teal-text); }
  .fill-lime { fill: var(--lime); }
  .fill-ink { fill: var(--ink); }
  .rule-white { stroke: var(--white); stroke-width: 2; }
  .rule-ink { stroke: var(--ink); stroke-width: 1.2; }
</style>
</head>
<body>
<svg class="signage-sheet" viewBox="0 0 1200 1200" xmlns="http://www.w3.org/2000/svg">
  <defs>
    <linearGradient id="foamPhotoTone" x1="0" y1="0" x2="1" y2="1">
      <stop offset="0" stop-color="var(--photo-dark)"/>
      <stop offset="0.55" stop-color="#9aa1a6"/>
      <stop offset="1" stop-color="var(--photo-light)"/>
    </linearGradient>
  </defs>

  <!-- Product banner -->
  <g class="sign product-banner">
    <rect class="panel-white" x="288" y="49" width="624" height="312"/>
    <path role="img" aria-label="Photo of a white car being sprayed with foam wash" fill="url(#foamPhotoTone)"
          d="M720 49 Q628 150 622 361 L912 361 L912 49 Z"/>
    <path d="M720 49 Q640 120 622 205" fill="none" stroke="var(--teal)" stroke-width="6"/>
    <path d="M646 230 Q614 290 620 361" fill="none" stroke="var(--lime)" stroke-width="7"/>
    <circle class="fill-lime" cx="446" cy="125" r="40"/>
    <text class="brand-name fill-lime" x="446" y="230" text-anchor="middle" font-size="40" textLength="210" lengthAdjust="spacingAndGlyphs">VERDALIA</text>
    <text class="headline fill-teal-text" x="445" y="278" text-anchor="middle" font-size="18">PREMIUM</text>
    <text class="headline fill-teal-text" x="445" y="298" text-anchor="middle" font-size="18" textLength="262" lengthAdjust="spacingAndGlyphs">ENVIRONMENT-FRIENDLY</text>
    <text class="headline fill-teal-text" x="445" y="318" text-anchor="middle" font-size="18" textLength="178" lengthAdjust="spacingAndGlyphs">BIODEGRADABLE</text>
    <line class="rule-ink" x1="315" y1="325" x2="578" y2="325"/>
    <text class="caption fill-ink" x="446" y="338" text-anchor="middle" font-size="10.5" textLength="260" lengthAdjust="spacingAndGlyphs">FOAM WASH AND CLEANING PRODUCTS</text>
    <line class="rule-ink" x1="315" y1="343" x2="578" y2="343"/>
  </g>

  <!-- Direction sign -->
  <g class="sign direction-sign">
    <rect class="panel-green" x="327" y="408" width="546" height="272"/>
    <text class="brand-name fill-white" x="600" y="535" text-anchor="middle" font-size="86" textLength="457" lengthAdjust="spacingAndGlyphs">VERDALIA</text>
    <g class="petal-arrows fill-white">
      <path d="M366 623 Q380 606 402 604 Q396 623 402 642 Q380 640 366 623 Z"/>
      <path d="M404 623 Q418 606 440 604 Q434 623 440 642 Q418 640 404 623 Z"/>
      <path d="M442 623 Q456 606 478 604 Q472 623 478 642 Q456 640 442 623 Z"/>
    </g>
    <text class="headline fill-white" x="828" y="637" text-anchor="end" font-size="36" textLength="338" lengthAdjust="spacingAndGlyphs">FOAM CAR WASH</text>
  </g>

  <!-- Wash bay sign -->
  <g class="sign wash-bay-sign">
    <rect class="panel-green" x="186" y="722" width="827" height="164"/>
    <rect class="band-teal" x="186" y="886" width="827" height="42"/>
    <circle class="fill-white" cx="295" cy="804" r="44"/>
    <text class="brand-name fill-white" x="641" y="841" text-anchor="middle" font-size="104" textLength="553" lengthAdjust="spacingAndGlyphs">VERDALIA</text>
    <text class="headline fill-ink" x="600" y="920" text-anchor="middle" font-size="33" letter-spacing="6">WASH BAY</text>
  </g>

  <!-- Location sign -->
  <g class="sign location-sign">
    <rect class="panel-green" x="47" y="986" width="1106" height="147"/>
    <circle class="fill-white" cx="160" cy="1060" r="40"/>
    <text class="brand-name fill-white" x="475" y="1093" text-anchor="middle" font-size="92" textLength="491" lengthAdjust="spacingAndGlyphs">VERDALIA</text>
    <line class="rule-white" x1="751" y1="1004" x2="751" y2="1121"/>
    <text class="headline fill-white" x="773" y="1078" font-size="38" textLength="329" lengthAdjust="spacingAndGlyphs">FOAM CAR WASH</text>
  </g>
</svg>
</body>
</html>
```